Layout for site fence advertising - length approx. 250 cm x 125 cm

The advertising will later be printed on a PVC film and used for events or on sports fields.

Main services :
Your regional contact at
Real estate and business financing
independent insurance advice

```html
<!DOCTYPE html>
<html lang="de">
<head>
<meta charset="utf-8">
<title>Falkner Vermögensberatung – Bauzaunbanner</title>
<link href="https://fonts.googleapis.com/css2?family=Comfortaa:wght@700&family=Poppins:wght@500;600;700&display=swap" rel="stylesheet">
<style>
  :root {
    --blue: #1a4fb8;
    --blue-deep: #123f9e;
    --blue-light: #2160cc;
    --white: #ffffff;
    --grey-wedge: #b4b6b8;
    --backdrop: #e6e7e9;
    --photo-bg: #f1f2f4;
  }
  * { margin: 0; padding: 0; box-sizing: border-box; }
  html, body { width: 972px; height: 1200px; overflow: hidden; }
  body { background: var(--backdrop); position: relative; font-family: "Poppins", sans-serif; }

  .banner {
    position: absolute; left: 26px; top: 370px;
    width: 920px; height: 460px; overflow: hidden;
    background: linear-gradient(135deg, var(--white) 0%, var(--photo-bg) 100%);
    box-shadow: 0 6px 18px rgba(0,0,0,.25);
  }
  .banner-shapes { position: absolute; inset: 0; }

  .portrait {
    position: absolute; left: 600px; top: 12px; width: 320px; height: 448px;
    background: linear-gradient(180deg, #e0b39c 0%, #d59c84 45%, #3a3b4a 75%, #2c2d3a 100%);
    border-radius: 140px 140px 0 0;
  }

  .brand { position: absolute; left: 46px; top: 48px; display: flex; align-items: center; }
  .brand-ring { width: 116px; height: 116px; border: 5px solid var(--white); border-radius: 50%; }
  .brand-divider { width: 3px; height: 122px; background: var(--white); margin: 0 10px 0 14px; }
  .brand-text { color: var(--white); font-family: "Comfortaa", sans-serif; font-weight: 700; }
  .brand-name { font-size: 19px; line-height: 1.3; }
  .brand-tagline { font-size: 14px; margin-top: 4px; }

  .intro-pill {
    position: absolute; left: 43px; top: 205px; width: 290px; height: 40px;
    border: 1.5px solid var(--white); border-radius: 20px;
    color: var(--white); font-weight: 600; font-size: 19px;
    display: flex; align-items: center; justify-content: center;
  }
  .intro-tail { position: absolute; left: 178px; top: 243px; }

  .service { position: absolute; left: 42px; display: flex; align-items: center; }
  .service-icon {
    width: 52px; height: 52px; border-radius: 50%; background: var(--white);
    box-shadow: -6px 6px 12px rgba(0,0,0,.25);
    display: flex; align-items: center; justify-content: center; margin-right: 16px;
  }
  .service-label { color: var(--white); font-weight: 600; font-size: 25px; line-height: 1.22; }
  .service-financing { top: 278px; }
  .service-insurance { top: 364px; }

  .contact {
    position: absolute; left: 610px; top: 361px; width: 310px; height: 73px;
    background: var(--blue); border-radius: 14px 0 0 14px;
    color: var(--white); padding: 8px 0 0 42px;
  }
  .contact-row { display: flex; align-items: center; gap: 8px; }
  .contact-phone { font-weight: 700; font-size: 29px; line-height: 1.15; }
  .contact-web { font-weight: 500; font-size: 18px; }
</style>
</head>
<body>
  <section class="banner">
    <svg class="banner-shapes" width="920" height="460" viewBox="0 0 920 460">
      <defs>
        <linearGradient id="blueFill" x1="0" y1="0" x2="1" y2="1">
          <stop offset="0" stop-color="#1c56c4"/>
          <stop offset="1" stop-color="#133f9c"/>
        </linearGradient>
      </defs>
      <polygon points="452,303 576,460 313,460" fill="var(--grey-wedge)"/>
      <path d="M0 0 H435 L528 82 Q578 124 545 166 L313 460 H0 Z" fill="url(#blueFill)"/>
    </svg>

    <div class="portrait" role="img" aria-label="Portrait photo of the advisor in a dark suit and white shirt"></div>

    <div class="brand">
      <div class="brand-ring"></div>
      <div class="brand-divider"></div>
      <div class="brand-text">
        <div class="brand-name">Falkner Vermögensberatung GmbH</div>
        <div class="brand-tagline">Finanzieren, Versichern, Vorsorgen</div>
      </div>
    </div>

    <div class="intro-pill">Your regional contact at</div>
    <svg class="intro-tail" width="22" height="14" viewBox="0 0 22 14">
      <path d="M0 1 L11 12 L22 1" fill="none" stroke="#fff" stroke-width="1.5"/>
    </svg>

    <div class="service service-financing">
      <div class="service-icon">
        <svg width="30" height="30" viewBox="0 0 30 30" fill="none" stroke="#1a4fb8" stroke-width="1.8" stroke-linejoin="round">
          <path d="M5 14 L15 5 L25 14 M8 12 V24 H22 V12"/>
          <rect x="12.5" y="17" width="5" height="7"/>
        </svg>
      </div>
      <div class="service-label">Real estate and<br>Business financing</div>
    </div>

    <div class="service service-insurance">
      <div class="service-icon">
        <svg width="30" height="30" viewBox="0 0 30 30" fill="none" stroke="#1a4fb8" stroke-width="1.8" stroke-linejoin="round">
          <path d="M15 4 L24 7 V14 C24 20 20 24 15 26 C10 24 6 20 6 14 V7 Z"/>
          <path d="M11 15 L14 18 L19 12"/>
        </svg>
      </div>
      <div class="service-label">Independent<br>Insurance advice</div>
    </div>

    <div class="contact">
      <div class="contact-row contact-phone">
        <svg width="18" height="18" viewBox="0 0 24 24"><circle cx="12" cy="12" r="12" fill="#fff"/><path d="M8 6 L10 6 L11 9 L9.5 10.5 C10.5 12.5 11.5 13.5 13.5 14.5 L15 13 L18 14 L18 16 C18 17 17 18 16 18 C10 17.5 6.5 14 6 8 C6 7 7 6 8 6 Z" fill="#1a4fb8"/></svg>
        <span>4321 987 654</span>
      </div>
      <div class="contact-row contact-web">
        <svg width="16" height="16" viewBox="0 0 24 24" fill="none" stroke="#fff" stroke-width="2"><circle cx="12" cy="12" r="10"/><path d="M2 12 H22 M12 2 C8 6 8 18 12 22 C16 18 16 6 12 2"/></svg>
        <span>www.falkner-finanz.de</span>
      </div>
    </div>
  </section>
</body>
</html>
```